Creative Brief
Brand Packaging Identity V
KALSO
Pose your way
Innovation and Creativity are the cornerstones in the foundation of KALSO. The most accurate quartz watches in the industry, ruggedized for use by those that live, work and play in truly adverse conditions. Water and Shock resistant, the line of technology used is advanced and inventive at the same time, for those whose usage demanded certain durability.
Jewelry
the back dial should consist of some art work as shown as an example in the briefing.

```html
<!DOCTYPE html>
<html lang="en">
<head>
<meta charset="utf-8">
<title>KALSO Packaging Identity</title>
<link href="https://fonts.googleapis.com/css2?family=Cinzel:wght@500&family=Lato:wght@400;700&display=swap" rel="stylesheet">
<style>
  :root{
    --ground:#2f2f30;
    --black:#0c0c0c;
    --gold:#c8ab74;
    --white:#f4f4f2;
    --line:#3a3a3a;
    --soft:#9a9a9a;
  }
  *{margin:0;padding:0;box-sizing:border-box}
  html,body{width:1200px;height:751px;overflow:hidden;background:var(--ground)}
  .canvas{position:relative;width:1200px;height:751px;font-family:"Lato",sans-serif}
  .piece{position:absolute}
  .panel{position:absolute;background:var(--black);border:1px solid var(--line)}
  .brand{font-family:"Cinzel",serif;font-weight:500;color:var(--gold);letter-spacing:.12em;display:flex;align-items:center;gap:6px;white-space:nowrap}
  .brand .dot{width:7px;height:7px;border-radius:50%;background:var(--gold)}
  .center{display:flex;align-items:center;justify-content:center}
  .tiny{font-size:6px;color:var(--soft);letter-spacing:.06em;white-space:nowrap}
  .vertical{writing-mode:vertical-rl}
  svg{position:absolute;left:0;top:0;width:100%;height:100%}
  .drop-content{position:absolute;inset:0;display:flex;flex-direction:column;align-items:center}
  .guarantee-band{background:var(--white);color:#222;font-size:15px;width:100%;text-align:center;padding:7px 0;margin-top:10px;white-space:nowrap}
  .form-row{display:flex;align-items:center;gap:5px;width:104px;margin-top:6px;font-size:7px;color:var(--white);white-space:nowrap}
  .form-row span{width:40px}
  .form-row i{flex:1;height:9px;background:var(--white)}
  .watch{position:absolute;border-radius:12px}
  .watch-light{background:radial-gradient(circle at 50% 45%,#ffffff 0 38%,#bdbdbd 40%,#1c1c1c 42%)}
  .watch-dark{background:radial-gradient(circle at 50% 45%,#151515 0 38%,#bdbdbd 40%,#1c1c1c 42%)}
  .ruler{position:absolute;display:flex;gap:2px}
  .ruler i{width:14px;height:18px;background:var(--white)}
  .handle{position:absolute;border:2px solid var(--gold);border-bottom:none;border-radius:40px 40px 0 0}
</style>
</head>
<body>
<main class="canvas">

  <section class="piece guarantee-front" style="left:20px;top:98px;width:168px;height:200px">
    <svg viewBox="0 0 100 124" preserveAspectRatio="none"><path d="M50 0 C72 26 100 44 100 74 A50 50 0 0 1 0 74 C0 44 28 26 50 0Z" fill="var(--black)" stroke="#555" stroke-width=".6"/></svg>
    <div class="drop-content">
      <div class="brand" style="margin-top:52px;font-size:16px"><span class="dot"></span>KALSO</div>
      <div class="tiny" style="margin-top:2px">Kalso Watches</div>
      <div class="guarantee-band">Guarantee Card</div>
      <div class="tiny" style="margin-top:28px">www.kalsowatches.com</div>
    </div>
  </section>

  <section class="piece guarantee-back" style="left:198px;top:98px;width:168px;height:200px">
    <svg viewBox="0 0 100 124" preserveAspectRatio="none"><path d="M50 0 C72 26 100 44 100 74 A50 50 0 0 1 0 74 C0 44 28 26 50 0Z" fill="var(--black)" stroke="#555" stroke-width=".6"/></svg>
    <div class="drop-content">
      <div class="brand" style="margin-top:52px;font-size:13px"><span class="dot"></span>KALSO</div>
      <div style="margin-top:14px">
        <div class="form-row"><span>Date</span><i></i></div>
        <div class="form-row"><span>Dealer Name</span><i></i></div>
        <div class="form-row"><span>Serial No</span><i></i></div>
      </div>
      <div class="tiny" style="margin-top:22px">www.kalsowatches.com</div>
    </div>
  </section>

  <section class="piece box-dieline" style="left:418px;top:82px;width:172px;height:280px">
    <div class="panel" style="left:14px;top:0;width:144px;height:22px"></div>
    <div class="panel center" style="left:14px;top:22px;width:144px;height:52px"><span class="tiny vertical" style="transform:rotate(180deg)">KALSO</span></div>
    <div class="panel" style="left:0;top:74px;width:24px;height:142px"></div>
    <div class="panel center" style="left:24px;top:74px;width:124px;height:142px">
      <div class="brand" style="font-size:17px"><span class="dot"></span>KALSO</div>
    </div>
    <div class="panel" style="left:148px;top:74px;width:24px;height:142px"></div>
    <div class="panel center" style="left:14px;top:216px;width:144px;height:46px"><span class="tiny">www.kalsowatches.com</span></div>
    <div class="panel" style="left:14px;top:262px;width:144px;height:18px"></div>
  </section>
  <div class="ruler" style="left:425px;top:383px"><i></i><i></i><i></i><i></i><i></i><i></i><i></i></div>

  <section class="piece strips" style="left:654px;top:82px;width:200px;height:280px">
    <div class="panel" style="left:0;top:0;width:56px;height:270px;border:2px solid var(--white)"></div>
    <div class="panel center" style="left:64px;top:0;width:52px;height:270px">
      <div class="brand vertical" style="font-size:14px"><span class="dot"></span>KALSO</div>
    </div>
    <div class="piece center" style="left:136px;top:0;width:54px;height:270px;background:var(--white)">
      <div class="brand vertical" style="font-size:14px;color:#555"><span class="dot" style="background:#555"></span>KALSO</div>
    </div>
  </section>

  <div class="watch watch-light" role="img" aria-label="Photo of a KALSO watch with white dial and black leather strap" style="left:904px;top:80px;width:100px;height:196px"></div>
  <div class="watch watch-dark" role="img" aria-label="Photo of a KALSO watch with black dial and black leather strap" style="left:1034px;top:80px;width:100px;height:196px"></div>

  <section class="piece tag" style="left:876px;top:252px;width:86px;height:132px">
    <svg viewBox="0 0 100 124" preserveAspectRatio="none"><path d="M50 0 C72 26 100 44 100 74 A50 50 0 0 1 0 74 C0 44 28 26 50 0Z" fill="var(--white)"/><circle cx="50" cy="30" r="4" fill="var(--ground)"/></svg>
    <div class="drop-content"><div class="brand" style="margin-top:72px;font-size:10px;color:#777"><span class="dot" style="background:#777"></span>KALSO</div></div>
  </section>
  <section class="piece tag" style="left:972px;top:252px;width:86px;height:132px">
    <svg viewBox="0 0 100 124" preserveAspectRatio="none"><path d="M50 0 C72 26 100 44 100 74 A50 50 0 0 1 0 74 C0 44 28 26 50 0Z" fill="var(--black)" stroke="#555" stroke-width=".8"/><circle cx="50" cy="30" r="4" fill="var(--ground)"/></svg>
    <div class="drop-content">
      <div style="margin-top:66px;width:70%;height:12px;background:var(--white)"></div>
      <div class="brand" style="margin-top:6px;font-size:9px"><span class="dot"></span>KALSO</div>
    </div>
  </section>
  <section class="piece tag" style="left:1068px;top:252px;width:86px;height:132px">
    <svg viewBox="0 0 100 124" preserveAspectRatio="none"><path d="M50 0 C72 26 100 44 100 74 A50 50 0 0 1 0 74 C0 44 28 26 50 0Z" fill="var(--black)" stroke="#555" stroke-width=".8"/><circle cx="50" cy="30" r="4" fill="var(--ground)"/></svg>
    <div class="drop-content"><div class="brand" style="margin-top:72px;font-size:10px"><span class="dot"></span>KALSO</div></div>
  </section>

  <section class="piece cross-dieline" style="left:22px;top:370px;width:338px;height:350px">
    <div class="panel center" style="left:114px;top:0;width:108px;height:106px"><div class="brand" style="font-size:9px"><span class="dot"></span></div></div>
    <div class="panel" style="left:0;top:120px;width:106px;height:106px"></div>
    <div class="panel center" style="left:114px;top:120px;width:108px;height:106px"><div class="brand" style="font-size:13px"><span class="dot"></span>KALSO</div></div>
    <div class="panel" style="left:230px;top:120px;width:108px;height:106px"></div>
    <div class="panel" style="left:114px;top:240px;width:108px;height:110px"></div>
  </section>

  <section class="piece small-box" style="left:372px;top:456px;width:216px;height:228px">
    <div class="panel center" style="left:54px;top:0;width:108px;height:54px"><span style="width:7px;height:7px;border-radius:50%;background:var(--gold)"></span></div>
    <div class="panel" style="left:0;top:54px;width:54px;height:120px"></div>
    <div class="panel center" style="left:54px;top:54px;width:108px;height:120px"><div class="brand" style="font-size:13px"><span class="dot"></span>KALSO</div></div>
    <div class="panel" style="left:162px;top:54px;width:54px;height:120px"></div>
    <div class="panel" style="left:54px;top:174px;width:108px;height:54px"></div>
  </section>

  <section class="piece flat-bag panel" style="left:600px;top:420px;width:200px;height:300px">
    <div style="position:absolute;left:78px;top:26px;width:44px;height:16px;border-radius:8px;background:var(--ground)"></div>
    <div class="center" style="position:absolute;inset:0"><div class="brand" style="font-size:20px"><span class="dot"></span>KALSO</div></div>
    <div class="tiny" style="position:absolute;bottom:14px;width:100%;text-align:center">www.kalsowatches.com</div>
  </section>

  <section class="piece shopping-bag" style="left:816px;top:420px;width:360px;height:300px">
    <div class="handle" style="left:44px;top:0;width:86px;height:42px"></div>
    <div class="handle" style="left:228px;top:0;width:86px;height:42px"></div>
    <div class="panel" style="left:0;top:40px;width:22px;height:260px"></div>
    <div class="panel center" style="left:22px;top:40px;width:136px;height:260px"><div class="brand" style="font-size:14px"><span class="dot"></span></div></div>
    <div class="panel center" style="left:158px;top:40px;width:202px;height:260px">
      <div class="brand" style="font-size:20px"><span class="dot"></span>KALSO</div>
      <div class="tiny" style="position:absolute;bottom:14px">www.kalsowatches.com</div>
    </div>
  </section>

</main>
</body>
</html>
```